Modern card design needed for building development company

We are looking for a sharp modern new look for our business cards.
We are a New Zealand based company called TKV Ventures NZ LTD that specialises in subdividing large sections, housing and commercial buildings.
We have attached a photo of the current logo and would like to see it improved somehow as it looks a bit dated.
We are open to any colours.

Target Market(s)

Investors, Property buyers

Industry/Entity Type

Investment

Contact Information for Business Card

TKV VENTURES NZ LTD
www.tkvventuresnz.co.nz

Howard Pennick
Phone +64 21 843 192
Email hdpennick@fernmail.co.nz

Font styles to use
Serif
Sans Serif

Colors
0792cd
33a6d7
85cae6
6b449b
886aae
f04a50
ec1f27
f37122
f68d4d

Requirements
Must have
• Please try and make the logo more modern or if you have a similar one we would like to see it.

```html
<!DOCTYPE html>
<html lang="en">
<head>
<meta charset="utf-8">
<title>TKV Ventures NZ LTD – Business Card</title>
<link rel="stylesheet" href="https://fonts.googleapis.com/css2?family=Jost:wght@300;400&family=Montserrat:wght@700&family=Marcellus+SC&display=swap">
<style>
  :root {
    --page-bg: #ffffff;
    --card-bg: #6c7074;
    --text-light: #ffffff;
    --text-dark: #1d1a1b;
    --brand-name: #eeeaf2;
    --brand-square: #8a5a7a;
    --label-grey: #6c7074;
  }
  * { margin: 0; padding: 0; box-sizing: border-box; }
  html, body {
    width: 1200px; height: 1200px; overflow: hidden;
    background: var(--page-bg);
  }
  .canvas { position: relative; width: 1200px; height: 1200px; }
  .card {
    position: absolute; top: 77px; width: 520px; height: 897px;
    background: var(--card-bg);
  }
  .card--front { left: 86px; }
  .card--back { left: 640px; }
  .line {
    position: absolute; left: 0; width: 100%;
    text-align: center; white-space: nowrap;
    transform: translateY(-50%);
  }
  .contact { font-family: "Jost", sans-serif; font-weight: 300; color: var(--text-light); }
  .contact__name { top: 89px; font-size: 32px; }
  .contact__phone { top: 122px; font-size: 26px; }
  .contact__email { top: 153px; font-size: 21px; }
  .brand-name {
    top: 470px; font-family: "Jost", sans-serif; font-weight: 400;
    font-size: 34px; letter-spacing: 2px; color: var(--brand-name);
  }
  .brand-square {
    position: absolute; left: 185px; top: 550px;
    width: 150px; height: 150px; background: var(--brand-square);
  }
  .company {
    top: 797px; font-family: "Montserrat", sans-serif; font-weight: 700;
    font-size: 23px; letter-spacing: 1px; color: var(--text-dark);
  }
  .website {
    top: 829px; font-family: "Jost", sans-serif; font-weight: 400;
    font-size: 27px; color: var(--text-dark);
  }
  .services {
    font-family: "Jost", sans-serif; font-weight: 300;
    font-size: 27px; color: var(--text-light);
  }
  .services__1 { top: 161px; }
  .services__2 { top: 192px; }
  .services__3 { top: 253px; }
  .services__4 { top: 285px; }
  .services__5 { top: 317px; }
  .side-label {
    position: absolute; top: 1042px; transform: translate(-50%, -50%);
    font-family: "Marcellus SC", serif; font-size: 54px;
    letter-spacing: 5px; color: var(--label-grey); white-space: nowrap;
  }
  .side-label--front { left: 298px; }
  .side-label--back { left: 874px; }
</style>
</head>
<body>
<main class="canvas">
  <section class="card card--front">
    <p class="line contact contact__name">Howard Pennick</p>
    <p class="line contact contact__phone">+64 21 843 192</p>
    <p class="line contact contact__email">Email : hdpennick@fernmail.co.nz</p>
    <p class="line brand-name">TKV Ventures NZ LTD</p>
    <div class="brand-square"></div>
    <p class="line company">TKV VENTURES NZ LTD</p>
    <p class="line website">www.tkvventuresnz.co.nz</p>
  </section>

  <section class="card card--back">
    <p class="line services services__1">HOUSING</p>
    <p class="line services services__2">COMMERCIAL BUILDING</p>
    <p class="line services services__3">SPECIALISES</p>
    <p class="line services services__4">IN</p>
    <p class="line services services__5">SUB DIVIDING LARGE SECTION</p>
    <p class="line brand-name">TKV Ventures NZ LTD</p>
    <div class="brand-square"></div>
    <p class="line company">TKV VENTURES NZ LTD</p>
  </section>

  <p class="side-label side-label--front">FRONT</p>
  <p class="side-label side-label--back">BACK</p>
</main>
</body>
</html>
```